Zielgruppe
Bestattungen Angehörige von Verstorbenen
Bestattungshaus Lindmark
Ahornsteig 7
61399 Auental
www.bestattungshaus-lindmark.de
info@bestattungshaus-lindmark.de
Tel: 06173 / 4820517
Mobil: 0152 / 83740162 24 Std Erreichbarkeit
Aufgabenstellung
Über mich
Mein Name ist Wolfgang Brenner, ich kann auf eine langjährige Berufserfahrung als Humanbestatter zurückblicken.
Die Versorgung und Bestattung eines Verstobenen, ist für Angehörige ein sehr wichtiger Aspekt.
Daher habe ich es mir zur Aufgabe gemacht, Sie auf diesem Weg in Ruhe und mit Genauigkeit zu begleiten.
Was Sie im Trauerfall beachten müssen
Bitte Bewahren Sie ruhe.
Jeder Trauerfall erfordert gewisse Maßnahmen die man treffen muss da diese im Bestattungsgesetzt Festgehalten sind.
Bitte informieren Sie uns Zeitnah um alles wichtige vorab zu besprechen und den Ablauf der Überführung des Verstorbenen zu klären.
Ein ausführliches Gespräch erfolgt zu einen späteren Zeitpunkt wo alle weiteren Fragen Ihrerseits, der Ablauf der Trauerfeier und oder Beisetzung geplant werden.
Verstirb ein Mensch zuhause
Müssen Sie zunächst den Hausarzt, Hausärztlichenvertretungsdienst (116 117 ),
oder den Rettungsdienst ( 112 ) informieren. Dieser wird dann nach der ersten Leichenschau den Totenschein ausstellen, der für den weiteren Ablauf mit uns sehr wichtig ist.
Tritt der Tod jedoch im Krankenhaus,
Pflege & Altenheim ein kümmert sich die dortige Verwaltung um die Formalitäten.
Unsere Leistungen für Sie
Gerne übernehmen wir für Sie folgende Aufgaben:
Persönliche Beratung und Betreuung Überführung im In- und Ausland
Erledigung sämtlicher Formalitäten (z.B. Todesbescheinigung, Sterbeurkunde.)
Versorgung des Verstorbenen nach DIN EN 15017
Aufbahrung & Abschiednahme in unseren Räumlichkeiten.
Trauerdrucksachen ,Traueranzeigen
Beratung bei der Wahl der Bestattungsform und des Ortes der Beisetzung.
Alle Bestattungsformen und Grab Arten sind bei uns möglich
Terminabsprachen mit Pfarrer/Trauerrednern, Friedhofsverwaltung
Individuelle Gestaltung, Organisation und Betreuung der Trauer P..

```html
<!DOCTYPE html>
<html lang="de">
<head>
<meta charset="utf-8">
<title>Bestattungshaus Lindmark – Flyer</title>
<link rel="stylesheet" href="https://fonts.googleapis.com/css2?family=Open+Sans:ital,wght@0,400;0,600;1,600;1,700&family=Montserrat:ital,wght@1,600&display=swap">
<style>
  :root {
    --paper: #ffffff;
    --card-top: #fbfbfb;
    --card-bottom: #e6e6e6;
    --band: #646464;
    --gold: #d8bc82;
    --sand: #e5d3ab;
    --footer: #d9d9d9;
    --ink: #1e1e1e;
    --rule: #9a9a9a;
  }
  * { margin: 0; padding: 0; box-sizing: border-box; }
  html, body { width: 853px; height: 1200px; overflow: hidden; background: var(--paper); }
  body { position: relative; font-family: "Open Sans", Arial, sans-serif; color: var(--ink); }

  .footer-band { position: absolute; left: 66px; top: 990px; width: 716px; height: 112px; background: var(--footer); }
  .services-panel { position: absolute; left: 66px; top: 480px; width: 440px; height: 553px; background: var(--paper); border-bottom-left-radius: 60px; box-shadow: 0 4px 6px rgba(0,0,0,.12); }
  .notice-panel { position: absolute; left: 506px; top: 492px; width: 276px; height: 541px; background: var(--sand); border-bottom-right-radius: 60px; }
  .title-band { position: absolute; left: 66px; top: 300px; width: 716px; height: 192px; background: var(--band); }
  .intro-card { position: absolute; left: 66px; top: 125px; width: 716px; height: 217px; background: linear-gradient(var(--card-top), var(--card-bottom)); border-bottom-left-radius: 80px; }

  .brand { position: absolute; left: 96px; top: 196px; width: 220px; font-size: 17px; font-weight: 600; color: var(--ink); line-height: 1.2; }

  .about { position: absolute; left: 352px; top: 143px; width: 235px; font-size: 10px; line-height: 16.8px; letter-spacing: .1px; }
  .about h2 { font-size: 10px; font-style: italic; font-weight: 700; }

  .portrait { position: absolute; left: 596px; top: 126px; width: 156px; height: 187px; border-radius: 20px 0 20px 0; background: linear-gradient(160deg, #c9c9c9 0%, #9a9a9a 55%, #2c2c2e 100%); }

  .band-title { position: absolute; left: 94px; top: 376px; width: 662px; display: flex; align-items: center; gap: 10px; }
  .band-title::before, .band-title::after { content: ""; flex: 1; height: 1px; background: var(--rule); }
  .band-title h1 { font-family: "Montserrat", sans-serif; font-style: italic; font-weight: 600; font-size: 21.5px; color: var(--gold); white-space: nowrap; letter-spacing: -.2px; }

  .photo-frame { position: absolute; top: 435px; width: 154px; height: 104px; background: var(--paper); padding: 8px 9px 9px; box-shadow: 0 2px 6px rgba(0,0,0,.25); }
  .photo { width: 100%; height: 100%; }
  .photo-room { background: linear-gradient(180deg, #e8e6e2 0%, #b7a28a 55%, #6d5a48 100%); }
  .photo-car { background: linear-gradient(180deg, #aab8c9 0%, #c4cdd6 40%, #6d8a4c 62%, #55823a 100%); }
  .photo-candles { background: radial-gradient(ellipse at 50% 10%, #f3c987 0%, #7a5a3a 35%, #3e3a38 70%, #2b2a2a 100%); }
  .photo-decor { background: linear-gradient(180deg, #e9e4d6 0%, #c9c1a8 45%, #6f8a4c 70%, #8a5236 100%); }

  .services-heading { position: absolute; left: 97px; top: 569px; font-size: 14px; font-style: italic; font-weight: 700; letter-spacing: -.6px; }
  .service-list { position: absolute; left: 99px; top: 620px; width: 400px; list-style: none; font-size: 10px; line-height: 16.8px; }
  .service-list li { position: relative; padding-left: 9px; margin-bottom: 12.1px; }
  .service-list li::before { content: ""; position: absolute; left: 0; top: 8px; width: 3px; height: 3px; border-radius: 50%; background: var(--ink); }

  .closing { position: absolute; left: 97px; top: 943px; font-size: 8.4px; }
  .partner { position: absolute; left: 112px; top: 968px; display: flex; align-items: center; gap: 28px; }
  .partner-name { font-size: 12px; font-weight: 600; color: var(--ink); }
  .partner-note { font-size: 9.5px; font-style: italic; font-weight: 700; }

  .notice { position: absolute; left: 538px; top: 566px; width: 218px; }
  .notice h2 { font-size: 14.5px; font-style: italic; font-weight: 600; line-height: 17.5px; margin-bottom: 14px; }
  .notice h3 { font-size: 9px; font-style: italic; font-weight: 700; line-height: 16px; }
  .notice ul { list-style: none; font-size: 9.9px; line-height: 16.8px; letter-spacing: -.3px; }
  .notice li { position: relative; padding-left: 10px; margin-bottom: 17px; }
  .notice li::before { content: ""; position: absolute; left: 0; top: 8px; width: 3px; height: 3px; border-radius: 50%; background: var(--ink); }
  .notice strong { font-weight: 600; }

  .footer-col { position: absolute; top: 1048px; font-size: 8.5px; line-height: 11px; font-style: normal; }
  .footer-col strong { font-weight: 600; }
  .footer-address { left: 94px; }
  .footer-web { left: 332px; }
  .footer-phone { left: 570px; }
  .footer-phone .label { display: inline-block; width: 26px; }
</style>
</head>
<body>
  <div class="footer-band"></div>
  <div class="services-panel"></div>
  <div class="notice-panel"></div>
  <div class="title-band"></div>
  <div class="intro-card"></div>

  <div class="brand">Bestattungshaus Lindmark</div>

  <section class="about">
    <h2>Über mich :</h2>
    <p>Mein Name ist Wolfgang Brenner, ich kann auf eine langjährige Berufserfahrung als Humanbestatter zurückblicken.<br>
    Die Versorgung und Bestattung eines Verstobenen, ist für Angehörige ein sehr wichtiger Aspekt.<br>
    Daher habe ich es mir zur Aufgabe gemacht, Sie auf diesem Weg in Ruhe und mit Genauigkeit zu begleiten.</p>
  </section>

  <div class="portrait" role="img" aria-label="Porträtfoto des Bestatters im dunklen Anzug"></div>

  <div class="band-title"><h1>Bestattungen Angehörige von Verstorbenen</h1></div>

  <div class="photo-frame" style="left:94px"><div class="photo photo-room" role="img" aria-label="Foto des Beratungsraums mit Tisch und Regal"></div></div>
  <div class="photo-frame" style="left:263px"><div class="photo photo-car" role="img" aria-label="Foto des Bestattungswagens vor Landschaft"></div></div>
  <div class="photo-frame" style="left:432px"><div class="photo photo-candles" role="img" aria-label="Foto von Kerzen und einer Trauermappe"></div></div>
  <div class="photo-frame" style="left:601px"><div class="photo photo-decor" role="img" aria-label="Foto von Trauerdekoration mit Pflanzen und Laternen"></div></div>

  <h2 class="services-heading">Gerne übernehmen wir für Sie folgende Aufgaben:</h2>
  <ul class="service-list">
    <li>Persönliche Beratung und Betreuung Überführung im In- und Ausland</li>
    <li>Erledigung sämtlicher Formalitäten (z.B. Todesbescheinigung, Sterbeurkunde.)</li>
    <li>Versorgung des Verstorbenen nach DIN EN 15017</li>
    <li>Aufbahrung &amp; Abschiednahme in unseren Räumlichkeiten.</li>
    <li>Trauerdrucksachen ,Traueranzeigen<br>Beratung bei der Wahl der Bestattungsform und des Ortes der Beisetzung.</li>
    <li>Alle Bestattungsformen und Grab Arten sind bei uns möglich</li>
    <li>Terminabsprachen mit Pfarrer/Trauerrednern, Friedhofsverwaltung</li>
    <li>Individuelle Gestaltung, Organisation und Betreuung der Trauer Planung und</li>
    <li>Durchführung von Trauermusik oder auch die Bestellung eines Organisten</li>
    <li>Bestattungsvorsorge /Bestattungstreuhand</li>
  </ul>

  <p class="closing">Bei allen weiteren Fragen sprechen Sie uns an Wir sind gern für Sie da.</p>
  <div class="partner">
    <span class="partner-name">Stillgrund</span>
    <span class="partner-note">Wir sind Partner von Stillgrund.</span>
  </div>

  <section class="notice">
    <h2>Was Sie im Trauerfall beachten müssen:</h2>
    <h3>Bitte Bewahren Sie ruhe.</h3>
    <ul>
      <li>Jeder Trauerfall erfordert gewisse Maßnahmen die man treffen muss da diese im Bestattungsgesetzt Festgehalten sind.</li>
      <li>Bitte informieren Sie uns Zeitnah um alles wichtige vorab zu besprechen und den Ablauf der Überführung des Verstorbenen zu klären.</li>
    </ul>
    <h3>Verstirb ein Mensch zuhause</h3>
    <ul>
      <li>Müssen Sie zunächst den Hausarzt, Hausärztlichenvertretungsdienst <strong>(116 117 )</strong>, oder den Rettungsdienst <strong>( 112 )</strong> informieren. Dieser wird dann nach der ersten Leichenschau den Totenschein ausstellen, der für den weiteren Ablauf mit uns sehr wichtig ist.</li>
      <li>Tritt der Tod jedoch im Krankenhaus, Pflege &amp; Altenheim ein kümmert sich die dortige Verwaltung um die Formalitäten.</li>
    </ul>
  </section>

  <address class="footer-col footer-address">Bestattungshaus Lindmark<br>Ahornsteig 7<br>61399 Auental</address>
  <div class="footer-col footer-web">www.bestattungshaus-lindmark.de<br>info@bestattungshaus-lindmark.de</div>
  <div class="footer-col footer-phone"><span class="label">Tel:</span> <strong>06173 / 4820517</strong><br>Mobil: <strong>0152 / 83740162 24</strong> Std Erreichbarkeit</div>
</body>
</html>
```